RW Hollis LLC Business Card - Civil Engineering & Consulting Firm

We need a Business Card that is elegant, and masculine.  It is our Professional Civil Engineering & Consulting Company located in San Antonio TX (Not s construction or builder firm- no gears & no tool images please). We provide civil engineering services including  commercial site plans, grading and drainage plans, utility plans, hydraulics and hydrology, land planning, utility coordination, and other general civil engineering services related to commercial and residential development.
We have 2 existing Logos. We would like to convey reliability, strength, trustworthiness and attention to detail.  Blues and orange tones as per logo We are OK with the use of a darker blue in the mix.  We have 2 logo versions - Full Company Name Logo to go on the back of card, & Small Icon Logo for the front w/ personal Info.

Target Market(s)
Architects, Real Estate Developers, Other Strctural Engineers, Surveyers, General Contractors
Industry/Entity Type
Professional Civil Engineering
Contact Information for Business Card
Name, Position, Address, Cell & Office #, email, and company website
Font styles to use
Other font styles liked:
- Avian
Requirements
Should not have
- No Tools, No Gears, no Cranes, or Construction Equipment.

```html
<!DOCTYPE html>
<html lang="en">
<head>
<meta charset="utf-8">
<title>RW Hollis LLC Business Card</title>
<link rel="stylesheet" href="https://fonts.googleapis.com/css2?family=Montserrat:wght@300;400;500;700&display=swap">
<style>
  :root {
    --backdrop: #c8c9c8;
    --card: #000000;
    --blue: #6fa3d6;
    --orange: #f39a32;
    --white: #ffffff;
    --text-light: #e6e6e6;
  }
  * { margin: 0; padding: 0; box-sizing: border-box; }
  html, body {
    width: 1200px;
    height: 1200px;
    overflow: hidden;
    background: var(--backdrop);
    font-family: "Montserrat", Arial, sans-serif;
  }
  .card {
    position: absolute;
    left: 171px;
    width: 869px;
    height: 509px;
    background: var(--card);
    overflow: hidden;
  }
  .card-back { top: 71px; }
  .card-front { top: 613px; }

  /* Back: company name */
  .brand {
    position: absolute;
    left: 0;
    right: 0;
    top: 205px;
    text-align: center;
    color: var(--blue);
    font-weight: 400;
    font-size: 74px;
    letter-spacing: 10px;
    line-height: 1;
  }
  .base-rule {
    position: absolute;
    top: 457px;
    height: 7px;
  }
  .base-rule-orange { left: 8px; width: 224px; background: var(--orange); }
  .base-rule-blue { left: 232px; right: 0; background: var(--blue); }

  /* Front: personal info */
  .rule-top {
    position: absolute;
    left: 400px;
    top: 0;
    width: 7px;
    height: 198px;
    background: var(--blue);
  }
  .rule-side {
    position: absolute;
    left: 203px;
    top: 300px;
    width: 7px;
    bottom: 0;
    background: var(--orange);
  }
  .person-name {
    position: absolute;
    left: 62px;
    top: 215px;
    font-size: 27px;
    font-weight: 500;
    letter-spacing: 3.5px;
    line-height: 1;
  }
  .first-name { color: var(--blue); }
  .surname { color: var(--orange); }
  .position {
    position: absolute;
    left: 202px;
    top: 255px;
    color: var(--white);
    font-size: 24px;
    font-weight: 400;
    letter-spacing: 0.5px;
  }
  .contact {
    position: absolute;
    left: 256px;
    top: 322px;
    list-style: none;
    color: var(--text-light);
    font-size: 24px;
    font-weight: 300;
    line-height: 36.7px;
  }
  .contact-label {
    color: var(--orange);
    font-weight: 700;
  }
  .brand-small {
    position: absolute;
    right: 50px;
    top: 175px;
    display: flex;
    align-items: center;
    gap: 10px;
    color: var(--blue);
    font-size: 26px;
    font-weight: 400;
    letter-spacing: 3px;
  }
  .brand-small-square {
    width: 16px;
    height: 16px;
    background: var(--orange);
  }
</style>
</head>
<body>
  <section class="card card-back">
    <div class="brand">RW HOLLIS LLC</div>
    <div class="base-rule base-rule-orange"></div>
    <div class="base-rule base-rule-blue"></div>
  </section>

  <section class="card card-front">
    <div class="rule-top"></div>
    <div class="brand-small"><span class="brand-small-square"></span>RW HOLLIS</div>
    <div class="person-name"><span class="first-name">NAME</span> <span class="surname">SURNAME</span></div>
    <div class="position">POSITION</div>
    <div class="rule-side"></div>
    <ul class="contact">
      <li>Address. Building, City ZIP</li>
      <li><span class="contact-label">M:</span> 987 654322</li>
      <li><span class="contact-label">O:</span> 987 654 321</li>
      <li><span class="contact-label">E:</span> email@rwhollis.com</li>
    </ul>
  </section>
</body>
</html>
```